INSURANCE COMPANY POSTCARD

WE ARE A WELL KNOWN INSURANCE AGENCY WORKING UNDER NEW OWNERSHIP USING THE OLD OWNERS NAME STILL, AS OUR TINY COMMUNITY WOULDN'T BE ABLE TO UNDERSTAND THAT WE ARE THE SAME AS BEFORE, JUST A NEW OWNER. WE PROVIDE AUTO, HOME, COMMERCIAL, FLOOD AND EVENT INSURANCE.

Industry/Entity Type

Insurance

```html
<!DOCTYPE html>
<html lang="en">
<head>
<meta charset="utf-8">
<title>Hartwell Insurance Agency – Postcard</title>
<link href="https://fonts.googleapis.com/css2?family=Crimson+Text:ital,wght@0,400;0,600;1,600;1,700&family=Tinos:wght@400&display=swap" rel="stylesheet">
<style>
  :root{
    --stage:#6a6a6a;
    --paper:#f1f1f1;
    --green:#76c044;
    --slate:#97a0b8;
    --ink:#4a4a4a;
    --navy:#1f3b8c;
    --violet:#7a4ea3;
    --white:#ffffff;
  }
  *{box-sizing:border-box;margin:0;padding:0}
  html,body{width:1200px;height:1200px;overflow:hidden}
  body{background:var(--stage);position:relative;font-family:"Tinos",serif;color:var(--ink)}
  .card{position:absolute;background:var(--paper);overflow:hidden;box-shadow:0 12px 30px rgba(0,0,0,.35)}
  .card svg.shapes{position:absolute;inset:0}
  .front{left:620px;top:180px;width:560px;height:840px}
  .back{left:30px;top:390px;width:560px;height:430px}

  .brand{position:absolute;display:flex;align-items:center;gap:10px;color:var(--green);font-family:"Crimson Text",serif;font-weight:600}
  .brand-mark{border-radius:50%;background:var(--navy);flex:none}
  .brand-text{display:flex;flex-direction:column;line-height:.95}
  .front .brand{right:32px;top:48px}
  .front .brand-mark{width:52px;height:52px}
  .front .brand-name{font-size:56px}
  .front .brand-sub{font-size:30px}
  .back .brand{left:350px;top:36px;gap:6px}
  .back .brand-mark{width:26px;height:26px}
  .back .brand-name{font-size:26px}
  .back .brand-sub{font-size:14px}

  .photo{position:absolute;border:9px solid var(--white);box-shadow:0 6px 14px rgba(0,0,0,.25)}
  .photo-family{left:30px;top:170px;width:500px;height:265px;background:linear-gradient(120deg,#e9e4dc 0%,#d8b59a 40%,#c79c80 60%,#efe9e2 100%)}
  .photo-kiss{left:16px;top:685px;width:165px;height:100px;border-width:6px;background:linear-gradient(90deg,#3a2d27 0%,#c9946f 50%,#2e2622 100%)}
  .photo-park{left:48px;top:28px;width:256px;height:176px;transform:rotate(-10deg);border-width:8px;background:linear-gradient(160deg,#8a9a88 0%,#5f8a3c 45%,#77b140 100%)}

  .headline{position:absolute;font-family:"Crimson Text",serif;font-style:italic;font-weight:700;line-height:1.05}
  .headline .soft{color:var(--slate)}
  .headline .bright{color:var(--green)}
  .front .headline{left:150px;top:454px;font-size:38px}
  .back .headline{left:24px;top:240px;font-size:34px}

  .section-title{position:absolute;left:28px;top:552px;font-family:"Crimson Text",serif;font-style:italic;font-weight:700;font-size:24px;color:var(--green)}
  .copy{position:absolute;font-size:17.5px;line-height:22px;text-align:justify;color:var(--ink)}
  .copy-child{left:28px;right:24px;top:584px}
  .copy-family{left:196px;right:22px;top:684px;font-size:17px;line-height:21.5px}

  .back .copy-intro{left:26px;top:318px;width:300px;font-size:15px;line-height:18px;text-align:left}
  .contact{position:absolute;left:26px;top:362px;display:flex;align-items:center;gap:16px;font-size:15px;color:var(--green)}
  .contact-item{display:flex;align-items:center;gap:6px}
  .contact-dot{width:24px;height:24px;border-radius:50%;background:var(--navy);flex:none}
  .contact-phone{width:24px;height:24px;border-radius:50%;background:var(--violet);display:flex;align-items:center;justify-content:center;flex:none}
  .address{position:absolute;left:26px;top:398px;font-size:13px;color:var(--ink)}
</style>
</head>
<body>

<section class="card front" aria-label="Postcard front">
  <svg class="shapes" width="560" height="840" viewBox="0 0 560 840" aria-hidden="true">
    <rect x="0" y="0" width="560" height="18" fill="var(--slate)"/>
    <polygon points="0,18 100,18 0,125" fill="var(--slate)"/>
    <polygon points="0,410 0,200 75,145 110,285" fill="var(--slate)"/>
    <polygon points="560,165 560,445 500,360" fill="var(--green)"/>
    <line x1="0" y1="543" x2="345" y2="543" stroke="var(--slate)" stroke-width="2"/>
    <circle cx="345" cy="543" r="7" fill="var(--slate)"/>
    <line x1="228" y1="670" x2="560" y2="670" stroke="var(--green)" stroke-width="2"/>
    <circle cx="228" cy="670" r="7" fill="var(--green)"/>
    <polygon points="0,808 155,804 155,812 560,812 560,840 0,840" fill="var(--green)"/>
  </svg>

  <div class="brand">
    <span class="brand-mark"></span>
    <span class="brand-text"><span class="brand-name">Hartwell</span><span class="brand-sub">Insurance Agency</span></span>
  </div>

  <div class="photo photo-family" role="img" aria-label="Photo of a smiling father with his son, daughter and wife"></div>

  <h1 class="headline">
    <span class="soft">“Did you</span> <span class="bright">have</span><br>
    <span class="bright">secured</span> <span class="soft">Your life ?</span>
  </h1>

  <h2 class="section-title">Child Insurence</h2>
  <p class="copy copy-child">Lorem Ipsum is simply dummy text of the printing and typesetting industry. Lorem Ipsum has been the industry's standard dummy text ever since standard dummy text ever since</p>

  <div class="photo photo-kiss" role="img" aria-label="Photo of parents kissing their young child on the cheeks"></div>
  <p class="copy copy-family">Lorem Ipsum is simply dummy text of the printing and typesetting industry. Lorem Ipsum has been the industry's standard dummy text ever since standard dummy text ever since</p>
</section>

<section class="card back" aria-label="Postcard back">
  <svg class="shapes" width="560" height="430" viewBox="0 0 560 430" aria-hidden="true">
    <polygon points="0,92 175,40 185,78 0,142" fill="var(--green)"/>
    <line x1="335" y1="100" x2="335" y2="430" stroke="var(--slate)" stroke-width="2"/>
    <circle cx="335" cy="100" r="6" fill="var(--slate)"/>
    <line x1="250" y1="214" x2="318" y2="196" stroke="var(--green)" stroke-width="2"/>
    <circle cx="318" cy="196" r="6" fill="var(--green)"/>
    <polygon points="290,430 330,370 362,430" fill="var(--slate)"/>
    <polygon points="350,430 560,372 560,430" fill="var(--slate)"/>
  </svg>

  <div class="photo photo-park" role="img" aria-label="Photo of a family running hand in hand across a lawn"></div>

  <div class="brand">
    <span class="brand-mark"></span>
    <span class="brand-text"><span class="brand-name">Hartwell</span><span class="brand-sub">Insurance Agency</span></span>
  </div>

  <h2 class="headline">
    <span class="soft">“Lorem</span> <span class="bright">Ipsum is</span><br>
    <span class="soft">simply dummy</span><span class="bright">!</span>
  </h2>

  <p class="copy copy-intro">Lorem Ipsum is simply dummy text of the printing and typesetting industry.</p>

  <div class="contact">
    <span class="contact-item"><span class="contact-dot"></span>hartwellcover.com</span>
    <span class="contact-item">
      <span class="contact-phone">
        <svg width="14" height="14" viewBox="0 0 24 24" aria-hidden="true"><path fill="#fff" d="M6.6 10.8a15.1 15.1 0 0 0 6.6 6.6l2.2-2.2c.3-.3.7-.4 1-.2 1.1.4 2.3.6 3.6.6.6 0 1 .4 1 1V20c0 .6-.4 1-1 1A17 17 0 0 1 3 4c0-.6.4-1 1-1h3.5c.6 0 1 .4 1 1 0 1.3.2 2.5.6 3.6.1.3 0 .7-.2 1z"/></svg>
      </span>555.014.2290</span>
  </div>
  <p class="address">Lorem Ipsum | Lorem Ipsum- 00000</p>
</section>

</body>
</html>
```